Mail order Nursery needs banner for promoting perennials that compliment roses.

banner should be 1135 wide x165 tall. We have an existing one displayed but we are not happy with the way it is washed out. Use your creativity to give us something that pops. Would love to see some watercolor or some other form of image other than just words washed across a stock photo. Banner needs to read Perennial Companions for Roses or some variation of that. Colors need to compliment our current theme. You can view the page and banner I want to replace at www.meadowlarkbloomyard.com. The banner we want to replace has been uploaded to the pixel forum file drop box. Thanks for your help and I look forward to seeing what you guys come up with. EDIT: I don't think I was clear enough in by brief. This banner promotes the sale of plants that look good planted with roses. We are getting to many submissions that are using only roses as the backdrop. We are looking for different types of plants that you would grow in your garden to compliment your roses. Thanks for all your hard work.

Target Market(s)

Home owners between 30 and 65

Industry/Entity Type

Nursery

Colors
33a6d7
e667a6

Requirements
Must have
• Text promotion perennials that compliment roses.... does not have to be those exact words but get the point across
Should not have
• Stock Photos with simple text washed across it.

```html
<!DOCTYPE html>
<html lang="en">
<head>
<meta charset="utf-8">
<title>Perennial Companions for Roses</title>
<link href="https://fonts.googleapis.com/css2?family=Tenor+Sans&family=Great+Vibes&display=swap" rel="stylesheet">
<style>
  :root {
    --sky: #33a6d7;
    --rose: #e0449c;
    --paper: #f1e6d3;
    --paper-edge: #e2d2b6;
    --leaf-dark: #3f6a2c;
    --leaf: #6f9a3e;
    --bloom: #e667a6;
    --bloom-deep: #c82a6e;
  }
  html, body {
    margin: 0;
    padding: 0;
    width: 1200px;
    height: 174px;
    overflow: hidden;
    background: #ffffff;
  }
  .banner {
    position: relative;
    width: 1200px;
    height: 174px;
    overflow: hidden;
  }
  .garden-photo {
    position: absolute;
    inset: 0 0 0 480px;
    background:
      radial-gradient(ellipse 120px 70px at 14% 35%, var(--bloom) 0%, transparent 70%),
      radial-gradient(ellipse 90px 60px at 40% 20%, #f59ac5 0%, transparent 70%),
      radial-gradient(ellipse 140px 80px at 48% 75%, var(--bloom-deep) 0%, transparent 70%),
      radial-gradient(ellipse 110px 60px at 72% 35%, #f07fb6 0%, transparent 70%),
      radial-gradient(ellipse 70px 40px at 58% 8%, #d9233f 0%, transparent 70%),
      radial-gradient(ellipse 60px 40px at 90% 12%, #e9c33a 0%, transparent 70%),
      radial-gradient(ellipse 120px 80px at 92% 70%, var(--bloom) 0%, transparent 70%),
      linear-gradient(135deg, var(--leaf) 0%, var(--leaf-dark) 50%, var(--leaf) 100%);
  }
  .paper {
    position: absolute;
    left: 0;
    top: 0;
    width: 560px;
    height: 174px;
  }
  .title {
    position: absolute;
    left: 0;
    top: 0;
    width: 540px;
    height: 174px;
  }
  .title-main {
    position: absolute;
    left: 44px;
    top: 14px;
    margin: 0;
    font-family: "Tenor Sans", sans-serif;
    font-weight: 400;
    font-size: 77px;
    line-height: 1;
    letter-spacing: 1px;
    color: var(--sky);
  }
  .title-sub {
    position: absolute;
    left: 52px;
    top: 84px;
    margin: 0;
    white-space: nowrap;
  }
  .title-script {
    font-family: "Great Vibes", cursive;
    font-size: 66px;
    color: var(--rose);
  }
  .title-for {
    font-family: "Tenor Sans", sans-serif;
    font-size: 19px;
    color: var(--sky);
    margin: 0 4px 0 8px;
  }
  .title-roses {
    font-family: "Tenor Sans", sans-serif;
    font-size: 43px;
    color: var(--rose);
  }
</style>
</head>
<body>
  <div class="banner">
    <div class="garden-photo" role="img" aria-label="Photograph of a garden bed with pink stargazer lilies, pink mallow blooms, red and yellow flowers among green foliage"></div>

    <svg class="paper" viewBox="0 0 560 174" aria-hidden="true">
      <defs>
        <linearGradient id="paperTone" x1="0" y1="0" x2="1" y2="0">
          <stop offset="0" stop-color="#e8d9bf"/>
          <stop offset="0.2" stop-color="#f3e9d8"/>
          <stop offset="0.85" stop-color="#f1e6d3"/>
          <stop offset="1" stop-color="#e6d5b8"/>
        </linearGradient>
      </defs>
      <path d="M0 0 H524 L520 12 L528 24 L522 38 L530 52 L524 66 L532 80 L526 94 L534 108 L527 122 L535 136 L528 150 L536 162 L530 174 H0 Z"
            fill="var(--paper-edge)"/>
      <path d="M0 0 H518 L514 12 L521 24 L516 38 L523 52 L517 66 L525 80 L519 94 L527 108 L520 122 L528 136 L521 150 L529 162 L523 174 H0 Z"
            fill="url(#paperTone)"/>
    </svg>

    <div class="title">
      <h1 class="title-main">PERENNIAL</h1>
      <p class="title-sub"><span class="title-script">Companions</span><span class="title-for">FOR</span><span class="title-roses">ROSES</span></p>
    </div>
  </div>
</body>
</html>
```